Christmas Banner for frontpage of website

New online scarf store just opened needs a Christmas Banner stating Free Delivery (UK only). Also if it could incorporate guaranteed Christmas delivery if ordered before 18th (might be too wordy though?) I would really like it to bring some colour to the page. The page is currently black and white with a pink accent and is very simple which is why I would like something modern and elegant, simple but with some colour. It is a shopify store I understand the banner size should be 950px by 290px the website is www.velmorabay.co.uk

Target Market(s)

Ladies

Industry/Entity Type

Store

Requirements
Should not have
• Not to look tacky.

```html
<!DOCTYPE html>
<html lang="en">
<head>
<meta charset="utf-8">
<title>Velmora Bay – Christmas Free Delivery Banner</title>
<link rel="stylesheet" href="https://fonts.googleapis.com/css2?family=Quicksand:wght@300;400&family=La+Belle+Aurore&display=swap">
<style>
  :root {
    --page-bg: #ffffff;
    --banner-bg: #f1ebe6;
    --frame-line: #ffffff;
    --headline-pink: #c2546f;
    --rule: #ddd2cd;
    --body-grey: #7a7272;
    --note-crimson: #a8234b;
    --art-pink: #e48aa6;
    --art-pink-soft: #f0c6cf;
    --art-berry: #c43a48;
    --greeting-ink: #5a2e33;
  }
  * { margin: 0; padding: 0; box-sizing: border-box; }
  html, body {
    width: 1200px;
    height: 1000px;
    overflow: hidden;
    background: var(--page-bg);
  }
  .canvas {
    position: relative;
    width: 1200px;
    height: 1000px;
  }
  .banner {
    position: absolute;
    left: 122px;
    top: 364px;
    width: 950px;
    height: 290px;
    background: var(--banner-bg);
    overflow: hidden;
  }
  .banner__frame {
    position: absolute;
    inset: 0;
  }
  .offer {
    position: absolute;
    left: 40px;
    top: 60px;
    width: 450px;
    text-align: center;
    font-family: "Quicksand", sans-serif;
  }
  .offer__headline {
    font-weight: 300;
    font-size: 43px;
    letter-spacing: 0;
    color: var(--headline-pink);
    line-height: 1;
  }
  .offer__rule {
    width: 320px;
    height: 1px;
    margin: 24px auto 0 auto;
    background: var(--rule);
    border: 0;
  }
  .offer__detail {
    margin-top: 20px;
    font-weight: 300;
    font-style: italic;
    font-size: 16.5px;
    letter-spacing: 0.8px;
    color: var(--body-grey);
    white-space: nowrap;
  }
  .offer__note {
    position: absolute;
    left: 26px;
    top: 251px;
    font-family: "Quicksand", sans-serif;
    font-weight: 400;
    font-size: 18px;
    color: var(--note-crimson);
  }
  .artwork {
    position: absolute;
    left: 520px;
    top: 0;
    width: 430px;
    height: 290px;
  }
  .greeting {
    position: absolute;
    font-family: "La Belle Aurore", cursive;
    color: var(--greeting-ink);
    line-height: 1;
    white-space: nowrap;
  }
  .greeting__wish {
    left: 692px;
    top: 186px;
    font-size: 27px;
    transform: rotate(-4deg);
  }
  .greeting__year {
    left: 756px;
    top: 244px;
    font-size: 30px;
    font-weight: 400;
  }
</style>
</head>
<body>
  <div class="canvas">
    <section class="banner" aria-label="Christmas free delivery banner">
      <svg class="banner__frame" width="950" height="290" viewBox="0 0 950 290" aria-hidden="true">
        <path d="M30 9 C250 5 520 13 700 8 C800 6 880 10 920 12 C940 14 944 30 943 60 C941 130 945 200 942 258 C940 278 928 282 900 281 C700 279 450 285 240 281 C140 280 70 283 34 282 C12 281 8 268 9 240 C11 170 7 100 10 40 C11 18 16 10 30 9 Z"
              fill="none" stroke="var(--frame-line)" stroke-width="1.5" opacity="0.6"/>
      </svg>

      <svg class="artwork" viewBox="0 0 430 290" role="img"
           aria-label="Watercolour pomegranate on a bare branch with red berries">
        <defs>
          <radialGradient id="fruit-glow">
            <stop offset="0" stop-color="var(--art-pink)" stop-opacity="0.9"/>
            <stop offset="0.55" stop-color="var(--art-pink-soft)" stop-opacity="0.6"/>
            <stop offset="1" stop-color="var(--art-pink-soft)" stop-opacity="0"/>
          </radialGradient>
          <radialGradient id="berry-glow">
            <stop offset="0" stop-color="var(--art-berry)" stop-opacity="0.28"/>
            <stop offset="1" stop-color="var(--art-berry)" stop-opacity="0"/>
          </radialGradient>
        </defs>
        <ellipse cx="140" cy="175" rx="140" ry="90" fill="url(#berry-glow)"/>
        <circle cx="315" cy="118" r="90" fill="url(#fruit-glow)"/>
      </svg>

      <div class="offer">
        <h1 class="offer__headline">FREE DELIVERY!</h1>
        <hr class="offer__rule">
        <p class="offer__detail">guaranteed Christmas delivery if ordered before 18th</p>
      </div>
      <p class="offer__note">*UK only</p>

      <p class="greeting greeting__wish">Happy new Year!</p>
      <p class="greeting greeting__year">2015</p>
    </section>
  </div>
</body>
</html>
```